Bubble-Diagramm als Infografik für unseren Kunden aus der Immobilienbranche
Zielgruppe
Wir sind ein Software-Unternehmen mit Kunden aus allen Branchen. Ganz generell für unsere Homepage, konkret aber auch im Rahmen eines Kundenprojektes suchen wir ansprechende Beispiele und kreative Visualisierungen, wie Diagramme zu bestimmten Sachverhalten dargestellt werden können.
Aufgabenstellung
Wir möchten die Möglichkeiten darstellen, mit excelbasierten Diagrammtypen den gewissen „Wow-Effekt“ bei unseren Kunden hervorzurufen. Konkret geht es uns hier um die Erstellung eines Bubble-Diagramms. In einem Objektvergleich von Gewerbeimmobilien sollen drei Dimensionen (hier: Größe des Objekte, Gesamtmiete über die Laufzeit, effektive Miete je Quadratmeter) im Bubble-Diagramm dargestellt werden. Siehe hierzu Entwurf (.xls-Datei) anbei.
Eine Orientierung an unserem Firmenlayout (www.brenolux-net.de) ist ausdrücklich erwünscht. Die Grafik sollte aufgeräumt und klar wirken, ohne nüchtern zu sein, um auf der einen Seite mit der Form nicht vom Inhalt abzulenken, und sich auf der anderen Seite aber eben doch über die Form von der Konkurrenz, die nur mit Excel-Bordmitteln arbeitet, erkennbar abzuheben. Denkbar sind grundsätzlich auch Piktogramme oder vergleichbare, Inhalt transportierende Elemente im Graphik-Hintergrund oder in der Umrahmung, immer unter der Maßgabe, dass sie nicht zu verspielt daherkommen.
Technisch sind wir in der Lage, Excel-Diagramme auch „interaktiv“ zu gestalten, also nach Klick auf ein Diagrammelement ein Kontextmenü oder erweiterte Informationen einzublenden. Daher wünschen wir uns als Teil des Entwurfs, beispielhaft für eine Blase, die Darstellung so eines interaktiven Elements: eines Kontextmenüs / und oder eines Datenblatts.
Vorzugsweise soll die Grafik im Excel-Format zur Verfügung gestellt werden, das ist aber kein Must-have.

```html
<!DOCTYPE html>
<html lang="de">
<head>
<meta charset="utf-8">
<title>Effektivmiete je m² – Bubble-Diagramm</title>
<link rel="stylesheet" href="https://fonts.googleapis.com/css2?family=Barlow:wght@400;500;600;700&display=swap">
<style>
  :root {
    --page-bg: #e6e8eb;
    --panel-light: #ffffff;
    --panel-edge: #eeeeee;
    --title-blue: #2a8ad4;
    --axis-dark: #255e8e;
    --axis-light: #8cc2f4;
    --grid: #e4e6e9;
    --plate: #fbfbfb;
    --plate-side: #dedede;
    --label: #2a4f74;
    --sector-light: #4bb8e0;
    --sector-mid: #2d8ad2;
    --sector-dark: #26608f;
    --white: #ffffff;
    --marker: #3fd6f0;
  }
  html, body {
    margin: 0;
    padding: 0;
    width: 900px;
    height: 1200px;
    overflow: hidden;
    background: var(--page-bg);
    font-family: "Barlow", Arial, sans-serif;
  }
  .chart-panel {
    position: absolute;
    left: 0;
    top: 347px;
    width: 900px;
    height: 506px;
  }
  .chart-panel svg { display: block; width: 100%; height: 100%; }
  .chart-title { font-weight: 700; font-size: 42px; fill: var(--title-blue); }
  .axis-title { font-weight: 700; font-size: 42px; fill: var(--title-blue); }
  .tick-label { font-weight: 400; font-size: 33px; fill: var(--label); }
  .legend-text { font-size: 17px; fill: var(--label); }
  .info-big { font-weight: 700; font-size: 31px; fill: var(--white); }
  .info-caption { font-weight: 600; font-size: 7px; fill: var(--white); }
  .info-value { font-weight: 700; font-size: 12.5px; fill: var(--white); }
</style>
</head>
<body>
<main class="chart-panel">
  <svg viewBox="40 32 1420 798" xmlns="http://www.w3.org/2000/svg" role="img" aria-label="Bubble-Diagramm: Effektivmiete je m² über Gesamtmiete, Blasengröße zeigt die Objektgröße">
    <defs>
      <radialGradient id="panelGlow" cx="50%" cy="45%" r="70%">
        <stop offset="0" stop-color="var(--panel-light)"/>
        <stop offset="1" stop-color="var(--panel-edge)"/>
      </radialGradient>
      <radialGradient id="bubbleFill" cx="38%" cy="25%" r="80%">
        <stop offset="0" stop-color="#e8f5ff"/>
        <stop offset="0.25" stop-color="#7cc2ff"/>
        <stop offset="0.7" stop-color="#2e8cf0"/>
        <stop offset="1" stop-color="#1f6fd6"/>
      </radialGradient>
      <radialGradient id="bubbleShadow" cx="50%" cy="50%" r="50%">
        <stop offset="0" stop-color="#000" stop-opacity="0.18"/>
        <stop offset="1" stop-color="#000" stop-opacity="0"/>
      </radialGradient>
      <clipPath id="plateClip">
        <polygon points="100,575 600,272 1440,318 1135,662"/>
      </clipPath>
    </defs>

    <rect class="panel-bg" x="40" y="32" width="1420" height="798" fill="url(#panelGlow)"/>

    <text class="chart-title" x="88" y="196">Effektivmiete je m²</text>

    <!-- floor plate -->
    <g class="floor">
      <polygon points="100,575 1135,662 1135,672 100,585" fill="var(--plate-side)"/>
      <polygon points="1135,662 1440,318 1440,330 1135,672" fill="#e8e8e8"/>
      <polygon points="100,575 600,272 1440,318 1135,662" fill="var(--plate)"/>
      <g class="grid" clip-path="url(#plateClip)" stroke="var(--grid)" stroke-width="1.2">
        <line x1="100" y1="575" x2="1135" y2="662"/>
        <line x1="162" y1="537" x2="1173" y2="619"/>
        <line x1="225" y1="499" x2="1211" y2="576"/>
        <line x1="287" y1="461" x2="1250" y2="533"/>
        <line x1="350" y1="423" x2="1288" y2="490"/>
        <line x1="412" y1="385" x2="1326" y2="447"/>
        <line x1="475" y1="347" x2="1364" y2="404"/>
        <line x1="537" y1="310" x2="1402" y2="361"/>
        <line x1="170" y1="581" x2="650" y2="275"/>
        <line x1="260" y1="589" x2="730" y2="279"/>
        <line x1="350" y1="596" x2="810" y2="283"/>
        <line x1="440" y1="604" x2="890" y2="287"/>
        <line x1="530" y1="611" x2="970" y2="291"/>
        <line x1="700" y1="625" x2="1050" y2="295"/>
        <line x1="790" y1="633" x2="1130" y2="299"/>
        <line x1="880" y1="640" x2="1210" y2="304"/>
        <line x1="970" y1="648" x2="1290" y2="309"/>
        <line x1="1060" y1="656" x2="1370" y2="314"/>
      </g>
    </g>

    <!-- reference lines -->
    <g class="reference-lines" stroke="var(--axis-light)" stroke-width="2" fill="var(--axis-light)">
      <line x1="404" y1="405" x2="1255" y2="466"/>
      <line x1="590" y1="283" x2="1378" y2="328"/>
      <line x1="614" y1="593" x2="965" y2="305" stroke-width="3"/>
      <circle cx="1255" cy="466" r="5"/>
      <circle cx="1378" cy="328" r="4"/>
    </g>

    <!-- axes -->
    <g class="axes" stroke="var(--axis-dark)" fill="var(--axis-dark)">
      <line x1="177" y1="554" x2="590" y2="283" stroke-width="3.5"/>
      <line x1="177" y1="554" x2="1101" y2="637" stroke-width="4"/>
      <g stroke-width="1">
        <line x1="175" y1="554" x2="175" y2="432"/>
        <line x1="408" y1="405" x2="408" y2="298"/>
        <line x1="589" y1="283" x2="589" y2="220"/>
        <line x1="177" y1="554" x2="100" y2="604"/>
        <line x1="614" y1="593" x2="530" y2="665"/>
        <line x1="1101" y1="637" x2="1028" y2="720"/>
      </g>
      <circle cx="177" cy="554" r="8" stroke="none"/>
      <circle cx="404" cy="405" r="6.5" stroke="none"/>
      <circle cx="590" cy="283" r="4" stroke="none"/>
      <circle cx="614" cy="593" r="7.5" stroke="none"/>
      <circle cx="1101" cy="637" r="8" stroke="none"/>
    </g>

    <g class="tick-labels">
      <text class="tick-label" x="138" y="422">15 €</text>
      <text class="tick-label" x="377" y="293">20 €</text>
      <text class="tick-label" x="561" y="212" style="font-size:27px">25 €</text>
      <text class="tick-label" x="120" y="635">5 Mio €</text>
      <text class="tick-label" x="561" y="681">10 Mio €</text>
      <text class="tick-label" x="1061" y="722">15 Mio €</text>
    </g>

    <!-- bubbles -->
    <g class="bubbles">
      <ellipse cx="590" cy="478" rx="55" ry="8" fill="url(#bubbleShadow)"/>
      <ellipse cx="722" cy="454" rx="44" ry="7" fill="url(#bubbleShadow)"/>
      <ellipse cx="837" cy="439" rx="55" ry="8" fill="url(#bubbleShadow)"/>
      <ellipse cx="1133" cy="437" rx="68" ry="9" fill="url(#bubbleShadow)"/>
      <circle class="bubble" cx="590" cy="419" r="59" fill="url(#bubbleFill)"/>
      <circle class="bubble" cx="722" cy="408" r="46" fill="url(#bubbleFill)"/>
      <circle class="bubble bubble--active" cx="837" cy="381" r="58" fill="url(#bubbleFill)"/>
      <circle class="bubble" cx="1133" cy="365" r="72" fill="url(#bubbleFill)"/>
    </g>

    <!-- data sheet callout -->
    <g class="callout">
      <polyline points="837,322 837,272 1016,272 1016,252" fill="none" stroke="var(--axis-dark)" stroke-width="2"/>
      <circle cx="837" cy="327" r="7" fill="var(--white)" stroke="var(--marker)" stroke-width="2.5"/>
    </g>

    <g class="info-disc">
      <circle cx="1016" cy="155" r="97" fill="#e7e9ec" stroke="#cfd3d8" stroke-width="1"/>
      <circle cx="1016" cy="155" r="91" fill="var(--white)"/>
      <path d="M1016,155 L1016,67 A88,88 0 0 0 939.8,199 Z" fill="var(--sector-light)"/>
      <path d="M1016,155 L1016,67 A88,88 0 0 1 1092.2,199 Z" fill="var(--sector-mid)"/>
      <path d="M1016,155 L1092.2,199 A88,88 0 0 1 939.8,199 Z" fill="var(--sector-dark)"/>

      <text class="info-big" x="980" y="120" text-anchor="middle">M²</text>
      <text class="info-caption" x="976" y="137" text-anchor="middle">Effektivmiete</text>
      <text class="info-value" x="976" y="151" text-anchor="middle">20.30 €</text>

      <g class="icon-house" fill="var(--white)">
        <path d="M1049,92 L1065,106 L1061,106 L1061,119 L1037,119 L1037,106 L1033,106 Z"/>
        <rect x="1045" y="109" width="8" height="10" fill="var(--sector-mid)"/>
      </g>
      <text class="info-caption" x="1056" y="137" text-anchor="middle">Gesamtmiete</text>
      <text class="info-value" x="1059" y="151" text-anchor="middle">10 Mio €</text>

      <g class="icon-expand" fill="none" stroke="var(--white)" stroke-width="1.8">
        <rect x="1004" y="176" width="24" height="24" rx="2"/>
        <path d="M1009,195 L1023,181 M1017,181 L1023,181 L1023,187 M1009,189 L1009,195 L1015,195"/>
      </g>
      <text class="info-caption" x="1016" y="214" text-anchor="middle">Größe</text>
      <text class="info-value" x="1016" y="229" text-anchor="middle">8.500M²</text>
    </g>

    <!-- legend & axis title -->
    <g class="legend">
      <circle cx="119" cy="767" r="28" fill="url(#bubbleFill)"/>
      <text class="legend-text" x="160" y="772">Die Größe der Blasen zeigt die Objektgröße an.</text>
    </g>
    <text class="axis-title" x="815" y="775" text-anchor="middle">Gesamtmiete</text>
  </svg>
</main>
</body>
</html>
```